Boutique custom software development company needs new business card

Our nearly 20 year old custom software development company would like to better include the fact that we are now providing Bitcoin services. These new services are B2B include education (how to acquire and securely hold Bitcoin) and integrating Bitcoin payments into existing ecommerce sites or other existing systems. Please keep the card clean and simple. Attached is our current design and some other files. vexalon.example

Target Market(s)

businesses owners interested in long term relationship

Industry/Entity Type

Custom software development and Bitcoin

Contact Information for Business Card

Marcus Ellwood, marcus@vexalon.example, vexalon.example, (888) 555-VEXAL

Font styles to use
Other font styles liked:
• monospace

Requirements
Must have
• double-sided
Nice to have
• clean and simple
Should not have
• physical address

```html
<!DOCTYPE html>
<html lang="en">
<head>
<meta charset="utf-8">
<title>Vexalon Business Card</title>
<link rel="stylesheet" href="https://fonts.googleapis.com/css2?family=Montserrat:wght@400;600;700&display=swap">
<style>
  :root {
    --backdrop: #3b3b3b;
    --card: #131313;
    --edge-blue: #3b74d1;
    --brand-blue: #4178c8;
    --accent-orange: #f07a22;
    --text-light: #e9e9e9;
    --pattern-dark: #0c0c0c;
    --pattern-mid: #242424;
  }
  * { margin: 0; padding: 0; box-sizing: border-box; }
  html, body { width: 1200px; height: 801px; overflow: hidden; }
  body {
    background: var(--backdrop);
    font-family: "Montserrat", sans-serif;
    position: relative;
  }
  .card {
    position: absolute;
    top: 252px;
    width: 520px;
    height: 297px;
    background: var(--card);
    border-bottom: 3px solid var(--edge-blue);
    border-left: 2px solid var(--edge-blue);
    overflow: hidden;
  }
  .card-front { left: 50px; }
  .card-back { left: 630px; }

  .brand {
    position: absolute;
    left: 40px;
    top: 112px;
    width: 244px;
  }
  .brand-name {
    font-weight: 700;
    font-size: 42px;
    letter-spacing: 1px;
    color: var(--brand-blue);
    line-height: 1;
  }
  .brand-tagline {
    margin-top: 7px;
    font-size: 12px;
    color: var(--brand-blue);
    white-space: nowrap;
  }
  .brand-services {
    margin-top: 3px;
    font-size: 12px;
    font-weight: 600;
    color: var(--accent-orange);
    white-space: nowrap;
  }
  .divider {
    position: absolute;
    left: 292px;
    top: 70px;
    width: 1px;
    height: 158px;
    background: var(--brand-blue);
  }
  .contact {
    position: absolute;
    left: 312px;
    top: 92px;
  }
  .contact-name {
    font-weight: 700;
    font-size: 17px;
    color: var(--brand-blue);
    margin-bottom: 14px;
    letter-spacing: 0.5px;
    white-space: nowrap;
  }
  .contact-list { list-style: none; }
  .contact-item {
    display: flex;
    align-items: center;
    gap: 8px;
    font-size: 12.5px;
    color: var(--text-light);
    margin-bottom: 7px;
    white-space: nowrap;
  }
  .contact-icon { width: 11px; height: 11px; flex: none; }

  .back-pattern {
    position: absolute;
    inset: 0;
    background: linear-gradient(125deg, var(--pattern-dark) 0%, var(--pattern-mid) 45%, var(--pattern-dark) 100%);
  }
  .back-mark {
    position: absolute;
    left: 372px;
    top: 128px;
    width: 56px;
    height: 56px;
    background: var(--brand-blue);
  }
</style>
</head>
<body>
  <section class="card card-front">
    <div class="brand">
      <div class="brand-name">VEXALON</div>
      <div class="brand-tagline">developer of custom applications</div>
      <div class="brand-services">bitcoin education &amp; payments</div>
    </div>
    <div class="divider"></div>
    <div class="contact">
      <div class="contact-name">MARCUS ELLWOOD</div>
      <ul class="contact-list">
        <li class="contact-item">
          <svg class="contact-icon" viewBox="0 0 12 12"><path d="M2 1 L4.5 1 L5.5 3.5 L4 4.5 Q5 7 7.5 8 L8.5 6.5 L11 7.5 L11 10 Q6 11 2 6 Q1 3 2 1Z" fill="var(--accent-orange)"/></svg>
          (888) 555-VEXAL
        </li>
        <li class="contact-item">
          <svg class="contact-icon" viewBox="0 0 12 12"><rect x="0.5" y="2.5" width="11" height="7" fill="var(--accent-orange)"/><path d="M0.5 2.5 L6 6.5 L11.5 2.5" stroke="var(--card)" fill="none"/></svg>
          marcus@vexalon.example
        </li>
        <li class="contact-item">
          <svg class="contact-icon" viewBox="0 0 12 12"><circle cx="6" cy="6" r="5.5" fill="var(--accent-orange)"/><path d="M0.5 6 H11.5 M6 0.5 Q3 6 6 11.5 M6 0.5 Q9 6 6 11.5" stroke="var(--card)" stroke-width="0.8" fill="none"/></svg>
          vexalon.example
        </li>
      </ul>
    </div>
  </section>

  <section class="card card-back">
    <div class="back-pattern" role="img" aria-label="Repeating tonal brand pattern in glossy black"></div>
    <div class="back-mark"></div>
  </section>
</body>
</html>
```